Church needs a graphic design/flyer layout for upcoming series

I need a multi-purpose design for promoting both our upcoming series of messages and our fall kick-off event where we will launch the messages.

Our promotion will be printed on a two-sided. One side is simple and focuses on the series and the other side has details in regards to the event. I have provided an attachment example of what we did last time.

The design needs to be multi-purpose because it will be used for our sermon Power Points, placed on our website banner, social media, etc.

• Sermon series is called “Harbor Lanterns”
• The subtitle will be “What’s keeping you from God?”
• Our name logo should be on the graphic as well.
• The subject manner will revolve around common hurdles that people face about God and Christianity: The existence of God, the exclusivity of religion, Hell, the reliability of the Bible, Hypocrisy in the church, etc.
• Our mission is “Connecting Young Families to Christ” so our focus is to reach out to families while not being exclusive to others.
• Our target audience is families with school-aged kids.
• This series is an invitational focus so we want it to be appealing to non-church goers.
• It should be attention grabbing while not being too ‘edgy’

• The front of the card will most likely consist the Sermon Series Graphic, title & subtitle of the series, and perhaps our name logo somewhere on it.
• The back of the card will invite and give the basic information for the event so that the people will be encouraged to save the date and come to the event.
• Here are some things that could be included on that advertisement:
o The name of the event: “Westbrook Commons Open Day”
o The date and time of the event: Sept 23rd @ 10:30
o Features of the event:
 Free lunch
 Children’s program
 Bouncy Castle
 Start of the “Harbor Lanterns” messages.
 Sample of topics
o Information about the church: our website and address, etc
o Engaging pictures and graphics.
• The rest of the tone and manner are the same as the sermon series graphic.
The flyer will be 11X14, like a postcard size.

Target Market(s)

Young families who are spiritually curious but not committed church attenders.

Colors

Designer to choose colors to be used in the design.

Requirements
Nice to have
• A modern and professional looking design.
Should not have
• Anything offensive or not family friendly.

```html
<!DOCTYPE html>
<html lang="en">
<head>
<meta charset="utf-8">
<title>Harbor Lanterns – Westbrook Commons Open Day</title>
<link rel="stylesheet" href="https://fonts.googleapis.com/css2?family=Playfair+Display:wght@700&family=Caveat+Brush&family=Oswald:wght@300;400&family=Libre+Baskerville&display=swap">
<style>
  :root {
    --backdrop: #e4e4e4;
    --sun-light: #f6d84a;
    --sun-mid: #f2a623;
    --sun-deep: #e0621e;
    --ember: #c9421e;
    --title-dark: #5a2a22;
    --title-warm: #e8542a;
    --ink: #2a1a1c;
    --plum: #662a66;
    --plum-deep: #3f1845;
    --plum-glow: #a0346f;
    --white: #ffffff;
    --strip-text: #3a1c40;
  }
  * { margin: 0; padding: 0; box-sizing: border-box; }
  html, body { width: 1054px; height: 1200px; overflow: hidden; }
  body { background: var(--backdrop); position: relative; font-family: "Oswald", sans-serif; }

  .card { position: absolute; left: 194px; width: 666px; height: 522px; overflow: hidden; }
  .card--front { top: 64px; }
  .card--back { top: 612px; background: var(--white); }

  .scene { position: absolute; inset: 0; }
  .scene--sunset {
    background:
      radial-gradient(ellipse 55% 45% at 18% 12%, rgba(255,240,140,.85), transparent 70%),
      linear-gradient(180deg, var(--sun-light) 0%, var(--sun-mid) 45%, var(--sun-deep) 78%, var(--ember) 100%);
  }
  .scene--dusk {
    bottom: 48px;
    background:
      radial-gradient(ellipse 12% 8% at 35% 66%, rgba(230,150,200,.55), transparent 80%),
      linear-gradient(180deg, var(--plum) 0%, var(--plum) 45%, var(--plum-glow) 80%, var(--plum-deep) 100%);
  }

  .series-title {
    position: absolute; top: 160px; left: 0; right: 0; text-align: center;
    font-family: "Playfair Display", serif; font-weight: 700;
    font-size: 76px; line-height: .92; text-transform: uppercase; letter-spacing: -1px;
    background: linear-gradient(100deg, var(--title-dark) 20%, var(--title-warm) 80%);
    -webkit-background-clip: text; background-clip: text; color: transparent;
  }
  .series-subtitle {
    position: absolute; top: 318px; left: 0; right: 0; text-align: center;
    font-family: "Caveat Brush", cursive; font-size: 25px; color: var(--ink);
    text-transform: uppercase; letter-spacing: .5px;
  }

  .church-mark { position: absolute; left: 0; right: 0; text-align: center; }
  .church-mark__dot { display: block; width: 30px; height: 30px; border-radius: 50%; margin: 0 auto 4px; }
  .church-mark__name { font-family: "Libre Baskerville", serif; font-size: 9px; }
  .card--front .church-mark { top: 398px; }
  .card--front .church-mark__dot { background: var(--ink); }
  .card--front .church-mark__name { color: var(--ink); }
  .card--back .church-mark { top: 413px; }
  .card--back .church-mark__dot { background: var(--white); }
  .card--back .church-mark__name { color: var(--white); }

  .event-title {
    position: absolute; top: 130px; left: 20px; width: 330px; text-align: center;
    font-family: "Playfair Display", serif; font-weight: 700; color: var(--white);
    font-size: 50px; line-height: .96; text-transform: uppercase;
  }
  .event-date {
    position: absolute; top: 310px; left: 20px; width: 330px; text-align: center;
    font-family: "Caveat Brush", cursive; font-size: 20px; color: var(--white);
  }
  .features { position: absolute; top: 140px; left: 375px; width: 270px; color: var(--white); }
  .features__heading { font-weight: 300; font-size: 16px; text-transform: uppercase; margin-bottom: 14px; letter-spacing: .3px; }
  .features__list { list-style: none; }
  .features__item {
    position: relative; padding-left: 24px; font-weight: 300; font-size: 19px;
    line-height: 22.5px; text-transform: uppercase;
  }
  .features__item::before { content: ">"; position: absolute; left: 0; }

  .contact-strip {
    position: absolute; left: 0; right: 0; bottom: 0; height: 48px; background: var(--white);
    text-align: center; color: var(--strip-text); padding-top: 9px;
  }
  .contact-strip__address { font-weight: 400; font-size: 12px; letter-spacing: .3px; }
  .contact-strip__lines { font-weight: 400; font-size: 11px; letter-spacing: .3px; }
  .contact-strip__sep { margin: 0 8px; }
</style>
</head>
<body>
  <section class="card card--front">
    <div class="scene scene--sunset" role="img" aria-label="Golden sunset sky over layered hazy orange mountain ridges"></div>
    <h1 class="series-title">Harbor<br>Lanterns</h1>
    <p class="series-subtitle">What's keeping you from God?</p>
    <div class="church-mark">
      <span class="church-mark__dot"></span>
      <span class="church-mark__name">Westbrook Commons Church</span>
    </div>
  </section>

  <section class="card card--back">
    <div class="scene scene--dusk" role="img" aria-label="Purple dusk sky with a faint setting sun over misty violet mountain ridges"></div>
    <h2 class="event-title">Westbrook<br>Commons<br>Open Day</h2>
    <p class="event-date">SEPT 23RD @ 10:30</p>
    <div class="features">
      <p class="features__heading">Features of the event:</p>
      <ul class="features__list">
        <li class="features__item">Free lunch</li>
        <li class="features__item">Children’s program</li>
        <li class="features__item">Bouncy castle</li>
        <li class="features__item">Start of the “Harbor Lanterns” messages.</li>
        <li class="features__item">Sample of topics</li>
      </ul>
    </div>
    <div class="church-mark">
      <span class="church-mark__dot"></span>
      <span class="church-mark__name">Westbrook Commons Church</span>
    </div>
    <footer class="contact-strip">
      <p class="contact-strip__address">1180 MAPLE RIDGE ROAD, LAKEVIEW, ON L0K 2B3</p>
      <p class="contact-strip__lines">+1 555.014.2290<span class="contact-strip__sep">•</span>HELLO@WESTBROOKCOMMONS.CA<span class="contact-strip__sep">•</span>WWW.WESTBROOKCOMMONS.CA</p>
    </footer>
  </section>
</body>
</html>
```